Business Card Design

Needing a business card design similar to the business card that is attached.

Industry/Entity Type

Business

Contact Information for Business Card

Design similar to the b-cards that is attached.

```html
<!DOCTYPE html>
<html lang="en">
<head>
<meta charset="utf-8">
<title>Harbor Realty &amp; PugetGeoEnergy – Business Cards</title>
<link rel="stylesheet" href="https://fonts.googleapis.com/css2?family=Noto+Serif:wght@400;700&display=swap">
<style>
  :root {
    --backdrop: #e8e4de;
    --card: #ffffff;
    --ink: #1c1c1c;
    --realty-blue: #1b86d4;
    --realty-dark: #222222;
    --geo-green: #1f9a4a;
    --geo-accent: #e8531f;
    --card-shadow: 0 6px 14px rgba(0, 0, 0, 0.35);
  }
  html, body {
    margin: 0;
    padding: 0;
    width: 1200px;
    height: 900px;
    overflow: hidden;
    background: var(--backdrop);
    font-family: "Noto Serif", Georgia, serif;
    color: var(--ink);
  }
  .canvas {
    position: relative;
    width: 1200px;
    height: 900px;
  }
  .card {
    position: absolute;
    top: 143px;
    width: 359px;
    height: 612px;
    background: var(--card);
    box-shadow: var(--card-shadow);
    text-align: center;
  }
  .card--realty { left: 224px; }
  .card--geo { left: 617px; }

  .brand-mark {
    position: absolute;
    left: 50%;
    transform: translateX(-50%);
  }
  .brand-mark--square {
    top: 50px;
    width: 70px;
    height: 70px;
    background: var(--realty-blue);
    border-radius: 0;
  }
  .brand-mark--circle {
    top: 36px;
    width: 86px;
    height: 86px;
    border-radius: 50%;
    background: var(--geo-accent);
  }
  .brand-name {
    position: absolute;
    left: 0;
    right: 0;
    top: 136px;
    margin: 0;
    font-weight: 700;
    font-size: 28px;
    line-height: 36px;
    letter-spacing: 0.2px;
  }
  .card--realty .brand-name { color: var(--realty-dark); }
  .card--geo .brand-name { color: var(--geo-green); }

  .person {
    position: absolute;
    left: 0;
    right: 0;
    top: 279px;
  }
  .person__name {
    margin: 0;
    font-weight: 400;
    font-size: 21px;
    line-height: 28px;
  }
  .card--realty .person__name { color: var(--realty-blue); }
  .card--geo .person__name { color: var(--geo-green); }
  .person__title {
    margin: 0;
    font-size: 14.5px;
    line-height: 22px;
    font-weight: 700;
    color: var(--ink);
  }

  .contact {
    position: absolute;
    left: 0;
    right: 0;
    margin: 0;
    font-style: normal;
    font-size: 14px;
    line-height: 22.6px;
  }
  .card--realty .contact { top: 453px; }
  .card--geo .contact { top: 476px; }

  .website {
    position: absolute;
    left: 0;
    right: 0;
    top: 566px;
    margin: 0;
    font-size: 14px;
    line-height: 22px;
  }
</style>
</head>
<body>
<main class="canvas">

  <section class="card card--realty" aria-label="Harbor Realty business card">
    <div class="brand-mark brand-mark--square" aria-hidden="true"></div>
    <h1 class="brand-name">HARBOR REALTY, INC.</h1>
    <div class="person">
      <h2 class="person__name">Marcus Tesfaye</h2>
      <p class="person__title">Managing Broker</p>
    </div>
    <address class="contact">
      4820 S 212th St. # B200,<br>
      Auburn, WA 98001<br>
      P: (206) 555-0147<br>
      F: (253) 555-0192
    </address>
    <p class="website">www.harborrealtyinc.com</p>
  </section>

  <section class="card card--geo" aria-label="PugetGeoEnergy business card">
    <div class="brand-mark brand-mark--circle" aria-hidden="true"></div>
    <h1 class="brand-name">PugetGeoEnergy, Inc.</h1>
    <div class="person">
      <h2 class="person__name">Marcus Tesfaye</h2>
      <p class="person__title">M. E. &amp; Certified Geothermal Installer</p>
    </div>
    <address class="contact">
      4820 S 212th St. # B200,<br>
      Auburn, WA 98001<br>
      P: (206) 555-0147
    </address>
    <p class="website">www.harborrealtyinc.com</p>
  </section>

</main>
</body>
</html>
```